Prepare a modern, professional business card for Bramford Ledger Services (BLS) Our company is in the banking, compliance and finance industry. We provide kiosks, software integration, and compliance guidelines so that banks can "bank" Marijuana Dispensaries with TrevMon, Office of Halvern Affairs and NTRB approval.

Target Market(s)

Banks

Industry/Entity Type

Business

Contact Information for Business Card

Owen R Pelley
Bramford Ledger Services
Vice President
742 Quarry Ridge Road
Suite 310
Marlow Flats, NV 89402
owen@bramfordls.net
638-555-0147

Font styles to use
Sans Serif

Requirements
Nice to have
• I like the clean simple appearance of Quillon computers. Perhaps the three LETTERS of BLS can be the LOGO on the Card and the Company name could be incorporated in the contact information. Like colors of white, black and gray

```html
<!DOCTYPE html>
<html lang="en">
<head>
<meta charset="utf-8">
<title>Bramford Ledger Services – Business Card</title>
<link rel="stylesheet" href="https://fonts.googleapis.com/css2?family=Mulish:wght@400;700&display=swap">
<style>
  :root {
    --page-bg: #e6e4e1;
    --card-bg: #262626;
    --mark-grey: #6a6a6a;
    --name-grey: #616161;
    --detail-grey: #595959;
    --company-white: #f2f2f2;
  }
  html, body {
    margin: 0;
    padding: 0;
    width: 1200px;
    height: 1000px;
    overflow: hidden;
    background: var(--page-bg);
    font-family: "Mulish", sans-serif;
  }
  .business-card {
    position: absolute;
    left: 252px;
    top: 293px;
    width: 692px;
    height: 412px;
    border-radius: 18px;
    background: var(--card-bg);
  }
  .brand-mark {
    position: absolute;
    left: 34px;
    top: 104px;
    width: 314px;
    height: 204px;
    display: flex;
    align-items: center;
    justify-content: flex-start;
    font-family: "Mulish", sans-serif;
    font-weight: 700;
    font-size: 172px;
    line-height: 1;
    letter-spacing: -4px;
    color: var(--mark-grey);
  }
  .contact-line {
    position: absolute;
    left: 380px;
    margin: 0;
    white-space: nowrap;
    font-size: 16px;
    line-height: 20px;
    color: var(--detail-grey);
  }
  .person-name {
    top: 126px;
    font-size: 20px;
    line-height: 24px;
    font-weight: 700;
    color: var(--name-grey);
    letter-spacing: 0.2px;
  }
  .person-title { top: 149px; left: 383px; }
  .company-name { top: 194px; color: var(--company-white); }
  .address-street { top: 216px; }
  .address-city { top: 237px; }
  .contact-phone { top: 269px; }
  .contact-email { top: 290px; }
  .with-icon {
    display: flex;
    align-items: center;
    gap: 5px;
  }
  .with-icon svg {
    width: 13px;
    height: 13px;
    flex: none;
  }
</style>
</head>
<body>
  <div class="business-card">
    <div class="brand-mark">BLS</div>

    <p class="contact-line person-name">Owen R Pelley</p>
    <p class="contact-line person-title">Vice President</p>

    <p class="contact-line company-name">Bramford Ledger Services</p>
    <p class="contact-line address-street">742 Quarry Ridge Road Suite 310</p>
    <p class="contact-line address-city">Marlow Flats, NV 89402</p>

    <p class="contact-line contact-phone with-icon">
      <svg viewBox="0 0 24 24" aria-hidden="true">
        <path fill="#ffffff" d="M6.6 10.8c1.4 2.8 3.8 5.1 6.6 6.6l2.2-2.2c.3-.3.7-.4 1-.2 1.1.4 2.3.6 3.6.6.6 0 1 .4 1 1V20c0 .6-.4 1-1 1C10.6 21 3 13.4 3 4c0-.6.4-1 1-1h3.5c.6 0 1 .4 1 1 0 1.3.2 2.5.6 3.6.1.3 0 .7-.2 1l-2.3 2.2z"/>
      </svg>
      638-555-0147
    </p>
    <p class="contact-line contact-email with-icon">
      <svg viewBox="0 0 24 24" aria-hidden="true">
        <rect x="2" y="5" width="20" height="14" fill="#ffffff"/>
        <path d="M2 5l10 8 10-8" fill="none" stroke="#262626" stroke-width="2"/>
      </svg>
      owen@bramfordls.net
    </p>
  </div>
</body>
</html>
```